Halden Construction Inc Business Card Design

We want a business card that stands out; we build high end commercial interiors so card should be professional yet creative and have an architectural/design feel , very clean lines

We have 6 employees so we must be able to change the name, cell and email on each person's card
For the proof Paul Merriton is the president
Office Number is (555) 284-3916, Cell ( 555 ) 431-0827

4700 Calloway Lane Suite 305, Coral Ridge Gardens, FL 34190
www.haldenbuilds.com
CGC 374915 ( This license must legally be on card)

Target Market(s)

Asset Specialists , Developers, Building owners, architects, business owners

Industry/Entity Type

Construction Company

Contact Information for Business Card

We want a very high end clean look, must incorporate existing logo

Font styles to use
Other font styles liked:
• Gotham, trade gothic, Mrs. Eaves,modern 20, trim or designers' choice

Colors

Designer to choose colors to be used in the design.

Requirements
Must have
• Name, address, CGC 374915, www.haldenbuilds.com
• 4700 Calloway Lane Suite 305, Coral Ridge Gardens, FL 34190
• each persons name, cell phone and individual email address ie paulm@haldenbuilds.com

```html
<!DOCTYPE html>
<html lang="en">
<head>
<meta charset="utf-8">
<title>Halden Construction Inc – Business Card</title>
<link href="https://fonts.googleapis.com/css2?family=Montserrat:wght@500;600;700&display=swap" rel="stylesheet">
<style>
  :root {
    --navy: #2b2c6c;
    --green: #6abf45;
    --band-grey: #dcdcdc;
    --white: #ffffff;
    --backdrop: #ebebeb;
  }
  * { box-sizing: border-box; margin: 0; padding: 0; }
  html, body {
    width: 1200px; height: 1000px; overflow: hidden;
    background: var(--backdrop);
    font-family: "Montserrat", Arial, sans-serif;
  }
  .card {
    position: absolute; left: 287px;
    width: 625px; height: 357px;
    background: var(--white);
    overflow: hidden;
  }
  .card--front { top: 124px; }
  .card--back { top: 519px; }
  .card__shapes { position: absolute; inset: 0; }

  .wordmark { position: absolute; color: var(--navy); font-weight: 700; line-height: 1; }
  .wordmark__main { display: block; letter-spacing: 1px; }
  .wordmark__sub { display: block; letter-spacing: 4.5px; }
  .card--front .wordmark { left: 16px; top: 42px; }
  .card--front .wordmark__main { font-size: 34px; }
  .card--front .wordmark__sub { font-size: 10px; margin-top: 4px; letter-spacing: 4px; }
  .card--back .wordmark { left: 0; right: 0; top: 100px; text-align: center; }
  .card--back .wordmark__main { font-size: 54px; }
  .card--back .wordmark__sub { font-size: 15px; margin-top: 6px; letter-spacing: 6.5px; }

  .person { position: absolute; left: 14px; top: 136px; color: var(--navy); }
  .person__name { font-size: 22px; font-weight: 700; }
  .person__title { font-size: 15px; font-weight: 500; margin-top: 2px; }

  .contact {
    position: absolute; left: 390px; top: 270px;
    color: var(--white); font-size: 14.5px; font-weight: 500; line-height: 21px;
  }

  .company-details {
    position: absolute; left: 0; right: 0; top: 263px;
    text-align: center; color: var(--navy); font-weight: 600;
    font-size: 11.5px; line-height: 14.5px;
  }
  .company-details__licence { font-size: 13px; }
</style>
</head>
<body>
  <section class="card card--front">
    <svg class="card__shapes" width="625" height="357" viewBox="0 0 625 357">
      <polygon points="358,0 495,0 308,357 173,357" fill="var(--band-grey)"/>
      <polygon points="491,0 499,0 312,357 304,357" fill="var(--green)"/>
      <polygon points="499,0 625,0 625,357 312,357" fill="var(--navy)"/>
    </svg>
    <div class="wordmark">
      <span class="wordmark__main">HALDEN</span>
      <span class="wordmark__sub">CONSTRUCTION</span>
    </div>
    <div class="person">
      <p class="person__name">Paul Merriton</p>
      <p class="person__title">President</p>
    </div>
    <div class="contact">
      <p>Office: (555) 284-3916</p>
      <p>Cell: (555) 431-0827</p>
      <p>paulm@haldenbuilds.com</p>
    </div>
  </section>

  <section class="card card--back">
    <svg class="card__shapes" width="625" height="357" viewBox="0 0 625 357">
      <polygon points="0,0 3,0 186,357 0,357" fill="var(--navy)"/>
      <polygon points="3,0 9,0 192,357 186,357" fill="var(--green)"/>
      <polygon points="619,0 625,0 439,357 433,357" fill="var(--green)"/>
      <polygon points="625,0 625,357 439,357" fill="var(--navy)"/>
    </svg>
    <div class="wordmark">
      <span class="wordmark__main">HALDEN</span>
      <span class="wordmark__sub">CONSTRUCTION</span>
    </div>
    <div class="company-details">
      <p>4700 Calloway Lane Suite 305</p>
      <p>Coral Ridge Gardens, FL 34190</p>
      <p class="company-details__licence">CGC 374915</p>
      <p>www.haldenbuilds.com</p>
    </div>
  </section>
</body>
</html>
```